I challenge you to create Denmark's coolest roofing company website

We need to have a website created for our roofing company.

I have some pages that can be used as a starting point because there are some things we would like to have, one important thing is a roof calculator, in addition to that information about the company, pictures of tasks we have completed, links to Friendlio and Pictavoro pages.

reviews from rated, etc. should also be visible on the page.

we have lots of pictures, videos, logos,

we need to have a nice home page that is just a little cooler than the competitors.
we need to steal their customer. the page should be easy and clear but with a nice design.
an important thing is the calculator.
come up with some suggestions we are quite open as long as it is a nice design
Updates

I have made an update in the PDF file with some thoughts and wishes. The file has been uploaded.

Target Market(s)

20-60

Industry/Entity Type

carpenter - roofer

Coding

Coded - Design and coding required

Number of Pages Required

4 page

Font styles to use
Sans Serif

Colors
EB3D1F
EC4F4E
F09395
F8D3D4
FCEDEE

Requirements
Must have
• Roof calculator, nice design, easy to get around
Nice to have
• the competitors : https://mollerbyghuset.dk https://hvid-tegl.dk https://strandbyghuset.dk

```html
<!DOCTYPE html>
<html lang="da">
<head>
<meta charset="utf-8">
<title>Tagmesteren – Roof Calculator</title>
<link href="https://fonts.googleapis.com/css2?family=Poppins:wght@300;400;500;600;700&display=swap" rel="stylesheet">
<style>
:root{
  --red:#eb1c24;
  --red-soft:#fcedee;
  --ink:#2b2f33;
  --text:#3c3f44;
  --muted:#55595e;
  --page:#e9ebee;
  --panel:#dcdfe3;
  --white:#ffffff;
  --line:#cfd3d8;
  --dark:#23282d;
  --footer:#1f2327;
}
*{box-sizing:border-box;margin:0;padding:0}
html,body{width:1200px;height:2603px;overflow:hidden}
body{position:relative;background:var(--page);font-family:'Poppins',sans-serif;color:var(--text)}
.abs{position:absolute}

/* header */
.site-header{position:absolute;left:0;top:0;width:1200px;height:110px;background:var(--white);box-shadow:0 1px 4px rgba(0,0,0,.06)}
.brand{position:absolute;left:108px;top:44px;display:flex;align-items:center;gap:10px;font-weight:700;font-size:30px;color:var(--ink);letter-spacing:-.5px}
.brand-mark{width:18px;height:18px;background:var(--red)}
.main-nav{position:absolute;left:409px;top:66px;display:flex;gap:26px;font-size:15px;font-weight:500;color:var(--ink)}
.header-call{position:absolute;left:888px;top:9px;display:flex;align-items:center;gap:12px;font-size:19px;color:var(--ink)}
.call-icon{width:38px;height:38px;border:1px solid #c9cdd2;border-radius:50%;display:flex;align-items:center;justify-content:center}
.btn-contact{position:absolute;left:967px;top:53px;width:122px;height:49px;border-radius:25px;background:var(--red);color:var(--white);font-weight:600;font-size:17px;display:flex;align-items:center;justify-content:center}

/* hero */
.hero-mark{left:593px;top:172px;width:14px;height:14px;background:var(--red)}
.hero-title{left:0;width:1200px;top:200px;text-align:center;font-size:40px;font-weight:700;color:var(--ink)}
.hero-sub{left:0;width:1200px;top:269px;text-align:center;font-size:16px;color:var(--muted)}

/* calculator card */
.calc-card{left:111px;top:348px;width:978px;height:1364px;background:var(--white);border-radius:12px}
.calc-icon{left:571px;top:372px;width:60px;height:60px;border-radius:50%;background:var(--red);display:flex;align-items:center;justify-content:center}
.calc-title{left:0;width:1200px;top:448px;text-align:center;font-size:26px;font-weight:600;color:var(--ink)}
.calc-sub{left:0;width:1200px;top:496px;text-align:center;font-size:16px;color:var(--muted)}
.step-line{height:4px;top:575px}
.step-dot{width:42px;height:42px;border-radius:50%;top:556px;display:flex;align-items:center;justify-content:center;font-weight:600;font-size:18px}
.step-label{top:614px;font-size:18px;color:var(--text);text-align:center;width:240px}

.form-frame{left:148px;top:735px;width:904px;height:933px;border:1px solid var(--line);background:var(--white)}
.form-tab{left:433px;top:696px;width:334px;height:82px;background:var(--white);border-radius:6px;box-shadow:0 2px 12px rgba(0,0,0,.08);text-align:center;padding-top:12px}
.form-tab h3{font-size:21px;font-weight:600;color:var(--ink)}
.form-tab p{font-size:16px;color:var(--muted);margin-top:2px}
.field-label{font-size:20px;font-weight:500;color:var(--text)}
.field-input{border:1px solid #8f9399;height:49px;background:var(--white);font-size:16px;color:var(--muted);padding:0 16px;display:flex;align-items:center}
.dropzone{left:174px;top:857px;width:856px;height:183px;border:1px solid #5d6166;text-align:center;font-size:16px;color:var(--muted);padding-top:24px;line-height:28px}
.btn{top:1563px;width:183px;height:57px;border-radius:29px;color:var(--white);font-weight:600;font-size:18px;display:flex;align-items:center;justify-content:center}
.btn-back{left:405px;background:var(--dark)}
.btn-next{left:611px;background:var(--red)}

/* notes */
.notes{left:111px;top:1756px;width:978px;height:271px;background:var(--panel);border-radius:12px;padding:36px 41px}
.notes h2{font-size:28px;font-weight:600;color:var(--ink);margin-bottom:18px}
.notes li{list-style:none;display:flex;align-items:center;gap:14px;font-size:17px;color:var(--muted);height:39.5px}

/* footer */
.footer-bg{left:0;top:2080px;width:1200px;height:523px}
.footer-brand{left:118px;top:2240px;font-size:40px;font-weight:700;color:var(--white);display:flex;align-items:center;gap:12px}
.footer-brand .brand-mark{background:var(--white);width:22px;height:22px}
.footer-col h4{font-size:19px;font-weight:600;color:var(--white);margin-bottom:18px}
.footer-col li{list-style:none;font-size:16px;color:var(--white);line-height:29px}
.contact-row{display:flex;gap:12px;align-items:flex-start}
.footer-rule{left:111px;top:2482px;width:978px;height:1px;background:#4a4f55}
.copyright{left:113px;top:2517px;font-size:16px;color:var(--white)}
.social{top:2509px;width:43px;height:43px;border-radius:50%;border:1px solid #8a8f95;display:flex;align-items:center;justify-content:center}
.social span{width:14px;height:14px;border-radius:50%;background:var(--red)}
</style>
</head>
<body>

<header class="site-header">
  <div class="brand"><span class="brand-mark"></span>Tagmesteren</div>
  <nav class="main-nav"><span>New roof</span><span>Roof solutions</span><span>We build with</span><span>References</span><span>About us</span></nav>
  <div class="header-call">
    <span class="call-icon"><svg width="16" height="16" viewBox="0 0 24 24"><path fill="#eb1c24" d="M6.6 10.8a15 15 0 006.6 6.6l2.2-2.2c.3-.3.7-.4 1-.2 1.1.4 2.3.6 3.6.6.6 0 1 .4 1 1V20c0 .6-.4 1-1 1A17 17 0 013 4c0-.6.4-1 1-1h3.5c.6 0 1 .4 1 1 0 1.3.2 2.5.6 3.6.1.3 0 .7-.2 1z"/></svg></span>
    Call : 40 51 62 73
  </div>
  <div class="btn-contact">CONTACT</div>
</header>

<div class="abs hero-mark"></div>
<h1 class="abs hero-title">Roof Calculator</h1>
<p class="abs hero-sub">Get an Instant Price Estimate for your roofing project</p>

<section class="abs calc-card"></section>
<div class="abs calc-icon">
  <svg width="28" height="28" viewBox="0 0 24 24" fill="none" stroke="#fff" stroke-width="1.8"><rect x="4" y="2.5" width="16" height="19" rx="2"/><rect x="7" y="5.5" width="10" height="4"/><g fill="#fff" stroke="none"><rect x="7" y="12" width="2" height="2"/><rect x="11" y="12" width="2" height="2"/><rect x="15" y="12" width="2" height="2"/><rect x="7" y="16" width="2" height="2"/><rect x="11" y="16" width="2" height="2"/><rect x="15" y="16" width="2" height="2"/></g></svg>
</div>
<h2 class="abs calc-title">Tag Beregnet</h2>
<p class="abs calc-sub">Fa et øjeblikkeligt prisoverslag pa dit tagprojekt</p>

<div class="abs step-line" style="left:257px;width:348px;background:var(--red)"></div>
<div class="abs step-line" style="left:605px;width:338px;background:#d7dbe0"></div>
<div class="abs step-dot" style="left:236px;background:var(--red)"><svg width="18" height="18" viewBox="0 0 24 24"><path d="M4 12.5l5 5L20 6.5" fill="none" stroke="#fff" stroke-width="3.5"/></svg></div>
<div class="abs step-dot" style="left:584px;background:var(--red);color:#fff">2</div>
<div class="abs step-dot" style="left:922px;background:#d7dbe0;color:var(--ink)">3</div>
<div class="abs step-label" style="left:137px">Tag information</div>
<div class="abs step-label" style="left:485px">Dine Oplysninger</div>
<div class="abs step-label" style="left:823px">Prisoverslag</div>

<div class="abs form-frame"></div>
<div class="abs form-tab"><h3>Dine Oplysninger</h3><p>Upload bileder og kontaktinformation</p></div>

<label class="abs field-label" style="left:172px;top:811px">Upload Bileder af Cit Tag</label>
<div class="abs dropzone">
  <svg width="50" height="48" viewBox="0 0 50 48"><path d="M25 2L12 16h8v14h10V16h8z" fill="#9a9ea3"/><rect x="2" y="30" width="46" height="16" rx="3" fill="#9a9ea3"/><circle cx="36" cy="40" r="2" fill="#fff"/><circle cx="42" cy="40" r="2" fill="#fff"/></svg><br>
  Klik for at upload billeder<br>PNG, jPG op til 10VB
</div>

<label class="abs field-label" style="left:172px;top:1069px">Beskrivelse af Projekt (Valgfrit)</label>
<div class="abs field-input" style="left:174px;top:1116px;width:856px">Beskriv dit projek, Saerige ensaker eller spermat..</div>

<label class="abs field-label" style="left:172px;top:1188px">Navn *</label>
<label class="abs field-label" style="left:608px;top:1188px">Telefon *</label>
<div class="abs field-input" style="left:174px;top:1235px;width:423px">Dit fulde navn</div>
<div class="abs field-input" style="left:609px;top:1235px;width:422px">+45 12 34 56 78</div>

<label class="abs field-label" style="left:172px;top:1306px">Email *</label>
<div class="abs field-input" style="left:174px;top:1352px;width:856px">din@emmail.dk</div>

<label class="abs field-label" style="left:172px;top:1424px">Addresse *</label>
<div class="abs field-input" style="left:174px;top:1470px;width:856px">Vejnavn 123, 800c Arhus</div>

<div class="abs btn btn-back">TILBAGE</div>
<div class="abs btn btn-next">NAESTE &rsaquo;</div>

<section class="abs notes">
  <h2>Vigtigt at vide</h2>
  <ul>
    <li><svg width="14" height="14" viewBox="0 0 24 24"><path d="M3 12.5l6 6L21 6" fill="none" stroke="#eb1c24" stroke-width="4"/></svg>Dette er et esimat baseret pa gennemsnitspriser</li>
    <li><svg width="14" height="14" viewBox="0 0 24 24"><path d="M3 12.5l6 6L21 6" fill="none" stroke="#eb1c24" stroke-width="4"/></svg>Den endelige pris kan variere afhaebgigt af dit projekts specifikke behov</li>
    <li><svg width="14" height="14" viewBox="0 0 24 24"><path d="M3 12.5l6 6L21 6" fill="none" stroke="#eb1c24" stroke-width="4"/></svg>Vi tilbyder gratis besigtigelse og præcist tilbud</li>
    <li><svg width="14" height="14" viewBox="0 0 24 24"><path d="M3 12.5l6 6L21 6" fill="none" stroke="#eb1c24" stroke-width="4"/></svg>Alle priser er inklusiv moms</li>
  </ul>
</section>

<svg class="abs footer-bg" viewBox="0 0 1200 523" role="img" aria-label="Dark photo of a tiled roof behind the footer">
  <defs><linearGradient id="roofShade" x1="0" y1="0" x2="1" y2="1"><stop offset="0" stop-color="#2a2e33"/><stop offset="1" stop-color="#181b1e"/></linearGradient></defs>
  <polygon points="0,112 1200,0 1200,523 0,523" fill="var(--red)"/>
  <polygon points="0,118 1200,27 1200,523 0,523" fill="url(#roofShade)"/>
</svg>

<div class="abs footer-brand"><span class="brand-mark"></span>Tagmesteren</div>

<div class="abs footer-col" style="left:527px;top:2222px">
  <h4>Overview of roof types</h4>
  <ul><li>Eternit roof</li><li>Steel roof</li><li>Tiled roof</li><li>Concrete roof</li><li>Roofing sheet</li><li>New facade</li></ul>
</div>
<div class="abs footer-col" style="left:828px;top:2222px">
  <h4>Contact Us</h4>
  <ul>
    <li class="contact-row"><svg width="11" height="16" viewBox="0 0 12 18" style="margin-top:6px"><path d="M6 0a6 6 0 00-6 6c0 4.5 6 12 6 12s6-7.5 6-12a6 6 0 00-6-6zm0 8.5A2.5 2.5 0 116 3.5a2.5 2.5 0 010 5z" fill="#eb1c24"/></svg><span>Tagmesteren ApS<br>Bakkelundvej 12<br>4200 Egedal</span></li>
    <li class="contact-row" style="margin-top:29px"><svg width="14" height="14" viewBox="0 0 24 24" style="margin-top:7px"><path fill="#eb1c24" d="M6.6 10.8a15 15 0 006.6 6.6l2.2-2.2c.3-.3.7-.4 1-.2 1.1.4 2.3.6 3.6.6.6 0 1 .4 1 1V20c0 .6-.4 1-1 1A17 17 0 013 4c0-.6.4-1 1-1h3.5c.6 0 1 .4 1 1 0 1.3.2 2.5.6 3.6.1.3 0 .7-.2 1z"/></svg><span>Call: 40 51 62 73</span></li>
  </ul>
</div>

<div class="abs footer-rule"></div>
<p class="abs copyright">© Copyright 2025, Tagmesteren. All rights reserved.</p>
<a class="abs social" style="left:993px" aria-label="Friendlio"><span></span></a>
<a class="abs social" style="left:1045px" aria-label="Pictavoro"><span></span></a>

</body>
</html>
```